New Crowdfunding site Fundlark needs banner ads

I’m looking for 4 standard size banner ads for www.fundlark.example to be used by TradeQuill Affiliates in order to bring new crowdfunding projects to the platform.
728x90
160x600
300x250
180x160

Succesful designers will put on our Mentors list so that the project owner can also get their specific project banners from our designers. Designers can also become our affiliates either to promote Fundlark.example or individual projects.
Updates

Please note updated brief

Thank you to those that have submitted designs so far.
Please be reminded that the invitation will close tomorrow after which we will make our choice

Thanks for input so far.
Please note project closes tomorrow (Sunday) after which we will choose.

Target Market(s)

Target is a project owner with a project requiring $10,000 or more in any field including business and/or non-profits. Any country.
Inventors, creatives, communities, hardware or software, consumer items,

Industry/Entity Type

Crowdfunding

Font styles to use
Sans Serif

Requirements
Must have
• Clear button call to action based on our USPs shown on the home page but especially the use of Affiliate Networks to promote their project to the widest possible audience.

Text and button text should be editable (see png preference).
Call to action could be based on "Free Crowdfunding Consultation - is your project viable" or "Get Your Free Guide to Succesful Crowdfunding"
Nice to have
• .png format preferred with separate objects.
Some animation preferred in the button.

```html
<!DOCTYPE html>
<html lang="en">
<head>
<meta charset="utf-8">
<title>Fundlark banner ad set</title>
<link href="https://fonts.googleapis.com/css2?family=Lato:wght@300;400;700;900&display=swap" rel="stylesheet">
<style>
  :root {
    --page: #ffffff;
    --cream: #f2f0de;
    --ink: #3a2818;
    --purple: #8e2687;
    --purple-edge: #5e1559;
    --green: #7dc242;
    --lime: #d9e22f;
    --white: #ffffff;
    --brand-blue: #3e4f9c;
    --label: #111111;
    --footer-edge: #e6e4d2;
    --hands: linear-gradient(160deg, #8e3a9e 0%, #e8327c 25%, #2aa7df 50%, #f08a24 72%, #8cc63f 100%);
  }
  * { box-sizing: border-box; margin: 0; padding: 0; }
  html, body { width: 1200px; height: 840px; overflow: hidden; background: var(--page); }
  body { position: relative; font-family: "Lato", sans-serif; color: var(--ink); }

  .banner { position: absolute; background: var(--cream); overflow: hidden; }
  .banner > * { position: absolute; }
  .size-label { position: absolute; font-size: 32px; font-weight: 400; color: var(--label); }

  .headline { text-transform: uppercase; font-weight: 300; line-height: 1; text-align: center; color: var(--ink); white-space: nowrap; }
  .headline .line { display: block; }
  .headline b { font-weight: 900; }

  .cta-tab {
    background: var(--green); color: var(--white); font-weight: 900; text-transform: uppercase;
    border-radius: 999px; text-align: center; z-index: 2; white-space: nowrap;
  }
  .cta-box {
    background: var(--purple); border: 2px solid var(--purple-edge); color: var(--white);
    text-transform: uppercase; font-weight: 700; text-align: center; line-height: 0.95;
    display: flex; flex-direction: column; justify-content: center; align-items: center;
    white-space: nowrap;
  }
  .cta-box .free { color: var(--lime); font-weight: 900; }

  .hands-art { background: var(--hands); opacity: 0.9; border-radius: 8px 8px 0 0; }

  .brand { display: flex; align-items: center; color: var(--brand-blue); font-weight: 400; white-space: nowrap; }
  .brand-dot { border-radius: 50%; background: var(--brand-blue); flex: none; }

  /* 160x600 */
  .sky { left: 24px; top: 18px; width: 204px; height: 758px; }
  .sky .headline { left: 0; width: 204px; top: 56px; font-size: 21px; letter-spacing: -0.3px; }
  .sky .headline .line { margin-bottom: 1px; }
  .sky .headline .big { font-size: 28px; }
  .sky .headline .mid { font-size: 22px; }
  .sky .headline .huge { font-size: 40px; margin-top: 2px; }
  .sky .cta-tab { left: 40px; top: 218px; width: 134px; font-size: 13px; padding: 3px 0; }
  .sky .cta-box { left: 13px; top: 227px; width: 178px; height: 176px; border-radius: 8px; font-size: 20px; padding-top: 10px; }
  .sky .cta-box .free { font-size: 70px; line-height: 0.9; }
  .sky .hands-art { left: 10px; top: 420px; width: 194px; height: 250px; }
  .sky .footer { left: 0; top: 670px; width: 204px; height: 88px; background: var(--white); border: 1px solid var(--footer-edge); border-top: 0; }
  .sky .brand { left: 8px; top: 690px; font-size: 23px; gap: 8px; }
  .sky .brand-dot { width: 50px; height: 50px; }

  /* 728x90 */
  .leader { left: 257px; top: 12px; width: 921px; height: 113px; }
  .leader .hands-art { left: 12px; top: 4px; width: 108px; height: 109px; }
  .leader .headline { left: 140px; top: 8px; width: 500px; font-size: 25px; letter-spacing: -0.3px; }
  .leader .cta-tab { left: 310px; top: 56px; width: 148px; font-size: 14px; padding: 2px 0; }
  .leader .cta-box { left: 136px; top: 63px; width: 496px; height: 40px; border-radius: 10px; font-size: 14px; flex-direction: row; gap: 4px; padding-top: 8px; }
  .leader .cta-box .free { font-size: 14px; }
  .leader .brand { left: 668px; top: 30px; font-size: 30px; gap: 8px; }
  .leader .brand-dot { width: 72px; height: 72px; }

  /* 300x250 */
  .rect { left: 261px; top: 183px; width: 383px; height: 318px; }
  .rect .headline { left: 0; width: 383px; top: 30px; font-size: 20px; letter-spacing: -0.3px; }
  .rect .headline .l2 { font-size: 17.5px; margin-top: 2px; }
  .rect .cta-tab { left: 108px; top: 76px; width: 168px; font-size: 16px; padding: 2px 0; }
  .rect .cta-box { left: 22px; top: 85px; width: 342px; height: 82px; border-radius: 10px; font-size: 18px; padding-top: 8px; }
  .rect .cta-box .free { font-size: 28px; }
  .rect .hands-art { left: 14px; top: 176px; width: 120px; height: 142px; }
  .rect .brand { left: 158px; top: 217px; font-size: 25px; gap: 8px; }
  .rect .brand-dot { width: 62px; height: 62px; }

  /* 180x160 */
  .small { left: 332px; top: 577px; width: 228px; height: 201px; }
  .small .headline { left: 0; width: 228px; top: 19px; font-size: 12px; letter-spacing: -0.3px; }
  .small .headline .l2 { font-size: 10.5px; margin-top: 1px; }
  .small .cta-tab { left: 64px; top: 45px; width: 98px; font-size: 9px; padding: 1px 0; }
  .small .cta-box { left: 13px; top: 51px; width: 205px; height: 49px; border-radius: 6px; font-size: 10px; padding-top: 6px; }
  .small .cta-box .free { font-size: 17px; }
  .small .hands-art { left: 14px; top: 106px; width: 80px; height: 95px; }
  .small .brand { left: 96px; top: 140px; font-size: 16px; gap: 5px; }
  .small .brand-dot { width: 36px; height: 36px; }
</style>
</head>
<body>

  <section class="banner sky" aria-label="Skyscraper banner 160 by 600">
    <h2 class="headline">
      <span class="line">Many people in</span>
      <span class="line">the world want</span>
      <span class="line big">to <b>help you</b></span>
      <span class="line mid">to fulfill <b>your</b></span>
      <span class="line huge"><b>dreams</b></span>
    </h2>
    <div class="cta-box"><span class="free">Free</span>Crowdfunding<br>consultation<br>is your<br>project viable</div>
    <div class="cta-tab">Click here for</div>
    <div class="hands-art" role="img" aria-label="Illustration of many colourful raised hands"></div>
    <div class="footer"></div>
    <div class="brand"><span class="brand-dot"></span>fundlark</div>
  </section>
  <div class="size-label" style="left:24px; top:786px;">160x600</div>

  <section class="banner leader" aria-label="Leaderboard banner 728 by 90">
    <div class="hands-art" role="img" aria-label="Illustration of many colourful raised hands"></div>
    <h2 class="headline">
      <span class="line">Many people in the world want</span>
      <span class="line"><b>to help you</b> to fulfill <b>your dreams</b></span>
    </h2>
    <div class="cta-box"><span class="free">Free</span> crowdfunding consultation - is your project viable</div>
    <div class="cta-tab">Click here for</div>
    <div class="brand"><span class="brand-dot"></span>fundlark</div>
  </section>
  <div class="size-label" style="left:260px; top:126px;">728x90</div>

  <section class="banner rect" aria-label="Medium rectangle banner 300 by 250">
    <h2 class="headline">
      <span class="line l1">Many people in the world want</span>
      <span class="line l2">to <b>help you</b> to fulfill <b>your dreams</b></span>
    </h2>
    <div class="cta-box"><span class="free">Free</span>Crowdfunding consultation<br>is your project viable</div>
    <div class="cta-tab">Click here for</div>
    <div class="hands-art" role="img" aria-label="Illustration of many colourful raised hands"></div>
    <div class="brand"><span class="brand-dot"></span>fundlark</div>
  </section>
  <div class="size-label" style="left:385px; top:508px;">300x250</div>

  <section class="banner small" aria-label="Small banner 180 by 160">
    <h2 class="headline">
      <span class="line l1">Many people in the world want</span>
      <span class="line l2">to <b>help you</b> to fulfill <b>your dreams</b></span>
    </h2>
    <div class="cta-box"><span class="free">Free</span>Crowdfunding consultation<br>is your project viable</div>
    <div class="cta-tab">Click here for</div>
    <div class="hands-art" role="img" aria-label="Illustration of many colourful raised hands"></div>
    <div class="brand"><span class="brand-dot"></span>fundlark</div>
  </section>
  <div class="size-label" style="left:385px; top:786px;">180x160</div>

</body>
</html>
```